Book cover required for new book business book (Otter Ambush SEO for Managed Service Providers)

We are finalizing publishing dates for our latest business book. The audience this book is targetting is IT business owners. Demographic age 30-50 years of age, male, middle class. The title of the book is Otter Ambush SEO for managed service providers. The author name is Dean Harrow. The book goes into details about how to improve SEO for IT businesses. The premise of the book is if a bear attacked a crowd of people, and you were in that crowd, you'd only have to be 1% faster to outrun the bear. The same is true for your IT Businesses website. You only have to put in 1% more effort into your SEO to be on page one of Zarvio.
We have been using a working draft image whilst the book has been in preproduction. I am unsure if this working image is licensed. Please find attached.

```html
<!DOCTYPE html>
<html lang="en">
<head>
<meta charset="utf-8">
<title>Otter Ambush SEO – Cover Wrap</title>
<link href="https://fonts.googleapis.com/css2?family=Roboto+Condensed:wght@400;700;800;900&family=Archivo:wght@800&display=swap" rel="stylesheet">
<style>
  :root{
    --cover-blue:#0f5aa8;
    --wave-mid:#3f86d8;
    --wave-light:#a9cdf5;
    --paper:#ffffff;
    --stage:#eef0f2;
    --ink:#0b0b0b;
  }
  *{margin:0;padding:0;box-sizing:border-box}
  html,body{width:899px;height:1200px;overflow:hidden;background:var(--stage)}
  .canvas{position:relative;width:899px;height:1200px}
  .wrap{
    position:absolute;left:20px;top:303px;width:859px;height:593px;
    background:var(--paper);overflow:hidden;
    box-shadow:0 2px 10px rgba(0,0,0,.12);
  }
  .wrap-art{position:absolute;inset:0;width:100%;height:100%}
  .back-copy{
    position:absolute;left:75px;top:30px;width:300px;
    font-family:"Roboto Condensed",sans-serif;font-weight:400;
    font-size:9.4px;line-height:13.2px;color:var(--paper);text-align:justify;
  }
  .back-copy p+p{margin-top:13px}
  .spine{
    position:absolute;left:396px;top:0;width:67px;height:593px;
  }
  .spine-title,.spine-author{
    position:absolute;left:50%;white-space:nowrap;
    transform-origin:0 0;
    font-family:"Roboto Condensed",sans-serif;font-weight:800;
  }
  .spine-title{
    top:60px;transform:rotate(90deg) translateY(-50%);
    font-size:32px;letter-spacing:-.5px;color:var(--paper);
  }
  .spine-author{
    top:372px;transform:rotate(90deg) translateY(-50%);
    font-size:19px;letter-spacing:7px;color:var(--ink);
  }
  .front{position:absolute;left:463px;top:0;width:396px;height:593px}
  .front-title{
    position:absolute;left:10px;right:10px;top:28px;text-align:center;
    white-space:nowrap;
    font-family:"Roboto Condensed",sans-serif;font-weight:900;
    font-size:43px;line-height:50px;letter-spacing:-1.5px;color:var(--ink);
    text-transform:uppercase;
    transform:scaleY(1.16);transform-origin:50% 0;
  }
  .front-subtitle{
    position:absolute;left:10px;right:10px;top:86px;text-align:center;
    white-space:nowrap;
    font-family:"Roboto Condensed",sans-serif;font-weight:700;
    font-size:19.5px;letter-spacing:.2px;color:var(--ink);
    text-transform:uppercase;
  }
  .front-author{
    position:absolute;left:0;right:0;top:532px;text-align:center;
    white-space:nowrap;
    font-family:"Archivo",sans-serif;font-weight:800;
    font-size:30px;letter-spacing:9px;color:var(--ink);
  }
</style>
</head>
<body>
<main class="canvas">
  <section class="wrap" aria-label="Book cover wrap: back, spine and front">
    <svg class="wrap-art" viewBox="0 0 859 593" xmlns="http://www.w3.org/2000/svg">
      <defs>
        <linearGradient id="waveFill" x1="0" y1="0" x2="1" y2="1">
          <stop offset="0" stop-color="var(--wave-light)"/>
          <stop offset=".45" stop-color="var(--wave-mid)"/>
          <stop offset="1" stop-color="var(--cover-blue)"/>
        </linearGradient>
      </defs>
      <path class="back-field" fill="var(--cover-blue)"
            d="M0 0H463V430C420 410 380 360 300 345C200 330 120 330 0 220Z"/>
      <path class="wave-band" role="img" aria-label="Flowing blue river wave sweeping across the cover"
            fill="url(#waveFill)" opacity=".85"
            d="M0 170C80 260 180 330 300 340C420 352 520 390 620 360C720 330 800 320 859 350V593C800 560 720 520 620 520C500 520 420 470 320 440C200 400 90 380 0 300Z"/>
      <rect class="fish-illustration" role="img" aria-label="White leaping fish illustration"
            x="256" y="300" width="134" height="100" rx="40" fill="var(--paper)" opacity=".9"/>
      <rect class="otter-illustration" role="img" aria-label="Large blue silhouette of an animal holding a fish"
            x="499" y="128" width="349" height="277" rx="60" fill="var(--cover-blue)"/>
    </svg>

    <div class="back-copy">
      <p>Lorem ipsum dolor sit amet, consectetur adipiscing elit. Sed tristique, arcu vitae facilisis posuere, libero ipsum laoreet est, eget efficitur risus risus et dui. Phasellus faucibus in ligula interdum semper. Nulla euismod dolor nec enim feugiat condimentum ut nec ex. Vestibulum id velit et lectus elementum accumsan eu in felis. Cras laoreet nibh a ipsum finibus, sed cursus mi lacinia. Duis ut convallis sem. Duis eu est leo. Donec tincidunt faucibus dolor. Quisque in feugiat dolor, ut scelerisque diam. Mauris laoreet consectetur ornare. Quisque bibendum volutpat dolor nec aliquet.</p>
      <p>Mauris eu volutpat mauris. Curabitur tincidunt sem eu egestas tincidunt. Proin vitae porta est. Duis ornare, dolor faucibus aliquet tincidunt, lacus elit dignissim lectus, eget pharetra sapien sapien ut ante. Duis quis dolor in lorem aliquam lacinia at et ante. Integer commodo turpis non massa tempor ullamcorper. Ut vel accumsan velit, ac gravida tellus. Cras tempus consectetur tempus. Nam molestie erat risus, vel cursus massa eleifend tincidunt. Cras ullamcorper tincidunt metus, aliquam hendrerit eros ultrices vitae. Aliquam viverra enim nec condimentum vehicula. Praesent aliquet varius dictum. Morbi molestie tellus est, quis tempor mi eleifend nec.</p>
    </div>

    <div class="spine">
      <span class="spine-title">OTTER AMBUSH SEO</span>
      <span class="spine-author">DEAN HARROW</span>
    </div>

    <div class="front">
      <h1 class="front-title">Otter Ambush SEO</h1>
      <p class="front-subtitle">For Managed Service Providers</p>
      <p class="front-author">DEAN HARROW</p>
    </div>
  </section>
</main>
</body>
</html>
```